Flyer für Immobilienmakler
Top Arbeit vom Designer. Er hat alle Idee schnell und professionell umgesetzt und das Ergebnis kann sich sehen lassen. Herzlichen Dank für die großartige Arbeit. Immer wieder gerne.
Zielgruppe
Immobilienmakler, Zielgruppe sind Menschen die uns weiterempfehlen um ihre Immobilie zu verkaufen
Aufgabenstellung
Ein Flyer DIN lang quer, Vorder und Rückseite, Es geht um eine Tippgeberprovision welche Menschen bekommen die uns einen Verkaufskunden bringen, diese erhalten 10 %- genaue Texte und Hinweise werde ich einbringen, Unser Slogan: 'Unsere Erfahrung für Ihren Vorteil'
Nachtrag. Bei dem Flyer 'Vom Berg Immobilien' finde ich die blauen Banner/ Streifen gut- ist aber kein Muss. Update: Es war als Inspiration von meiner Seite gedacht. Auf keinen Fall darf es genauso aussehen!!
Meine jetzige Webseite ist auch gut um die Farben zu erkennen, jedoch nicht unbedingt das Design, da ich gerade eine neue Webseite erstellen lasse

```html
<!DOCTYPE html>
<html lang="de">
<head>
<meta charset="UTF-8">
<title>Flyer – Tippgeberprovision</title>
<link href="https://fonts.googleapis.com/css2?family=Montserrat:wght@400;500;600&display=swap" rel="stylesheet">
<style>
  :root {
    --navy: #2c3160;
    --white: #ffffff;
    --page: #f6f6f6;
    --sky: #a9cdea;
    --facade: #ecede8;
    --foliage: #7da257;
  }
  * { margin: 0; padding: 0; box-sizing: border-box; }
  html, body {
    width: 1200px; height: 1200px; overflow: hidden;
    background: var(--page);
    font-family: "Montserrat", sans-serif;
  }
  .flyer {
    position: absolute; left: 40px; top: 320px;
    width: 1120px; height: 560px;
    background: var(--white);
    box-shadow: 0 4px 10px rgba(0,0,0,0.18);
  }
  .header-band {
    position: absolute; left: 0; top: 0; width: 100%; height: 75px;
    background: var(--navy);
  }
  .slogan {
    position: absolute; left: 27px; top: 0; height: 75px;
    display: flex; align-items: center;
    color: var(--white); font-weight: 500; font-size: 25px;
    letter-spacing: 4.3px; white-space: nowrap;
  }
  .brand-box {
    position: absolute; left: 849px; top: 0; width: 231px; height: 75px;
    background: var(--white);
    padding: 0 22px;
    display: flex; flex-direction: column; justify-content: center; align-items: flex-end;
    color: var(--navy); font-weight: 600; white-space: nowrap;
  }
  .brand-name { font-size: 31px; letter-spacing: 4px; line-height: 1; align-self: center; }
  .brand-sub { font-size: 11px; letter-spacing: 0.5px; margin-top: 3px; }
  .rule {
    position: absolute; left: 0; width: 100%; height: 2px; background: var(--navy);
  }
  .rule.top { top: 81px; }
  .rule.bottom { top: 502px; }
  .photo {
    position: absolute; left: 0; top: 89px; width: 100%; height: 409px;
    background: linear-gradient(160deg, var(--sky) 0%, var(--facade) 50%, var(--foliage) 100%);
  }
  .badge {
    position: absolute; left: 26px; top: 105px; width: 170px; height: 170px;
  }
  .footer-band {
    position: absolute; left: 0; bottom: 0; width: 100%; height: 47px;
    background: var(--navy);
    display: flex; align-items: center; justify-content: center;
    color: var(--white); font-size: 17px; letter-spacing: 1px;
  }
</style>
</head>
<body>
  <div class="flyer">
    <header class="header-band">
      <h1 class="slogan">UNSERE ERFAHRUNG FÜR IHREN VORTEIL</h1>
      <div class="brand-box">
        <span class="brand-name">AUREL</span>
        <span class="brand-sub">Immobilien</span>
      </div>
    </header>
    <div class="rule top"></div>
    <div class="photo" role="img" aria-label="Foto eines modernen weißen Mehrfamilienhauses mit Balkonen zwischen grünen Bäumen unter blauem Himmel"></div>
    <svg class="badge" viewBox="0 0 170 170" aria-label="10 Prozent Tippgeberprovision">
      <defs>
        <path id="ring" d="M85,85 m-68,0 a68,68 0 1,1 136,0 a68,68 0 1,1 -136,0"/>
        <path id="arc" d="M52,118 A48,48 0 0,0 132,68"/>
      </defs>
      <circle cx="85" cy="85" r="84" fill="#ffffff"/>
      <circle cx="85" cy="85" r="59" fill="none" stroke="#2c3160" stroke-width="1.2" stroke-dasharray="1 3"/>
      <text font-family="Montserrat, sans-serif" font-size="11.5" font-weight="600" fill="#2c3160" letter-spacing="2.2">
        <textPath href="#ring" startOffset="0">TIPPGEBERPROVISION · TIPPGEBERPROVISION ·</textPath>
      </text>
      <text x="80" y="100" text-anchor="middle" font-family="Montserrat, sans-serif" font-size="50" font-weight="500" fill="#2c3160" transform="rotate(-10 80 85)">10</text>
      <text font-family="Montserrat, sans-serif" font-size="11" fill="#2c3160" letter-spacing="2">
        <textPath href="#arc" startOffset="8">PROZENT</textPath>
      </text>
    </svg>
    <div class="rule bottom"></div>
    <footer class="footer-band">www.aurel-haus.de</footer>
  </div>
</body>
</html>
```